Law Enforcement SaaS

We're looking for a modern, somewhat minimalistic, business card layout to use for C-Suite interactions with customers in the public safety realm. We provide a patented information-sharing solution to law enforcement (can reference our company website at https://volmarex.com). The design should follow our current branding guide (attached as a reference with the logo) and focus on splashes of color to act as an accent. We intend to utilize the back of the card to highlight the product, and maybe insert a QR for our website. We're open to having a non-traditional design, so outside-the-box thinking is acceptable.

```html
<!DOCTYPE html>
<html lang="en">
<head>
<meta charset="utf-8">
<title>Volmarex Business Card</title>
<link rel="stylesheet" href="https://fonts.googleapis.com/css2?family=Montserrat:wght@400;500;800&display=swap">
<style>
  :root {
    --backdrop: #9c9c9c;
    --paper: #ffffff;
    --ink: #141a2b;
    --accent: #35bbec;
    --accent-deep: #3a8db3;
  }
  * { margin: 0; padding: 0; box-sizing: border-box; }
  html, body { width: 1093px; height: 1200px; overflow: hidden; }
  body {
    position: relative;
    background: var(--backdrop);
    font-family: "Montserrat", Arial, sans-serif;
    color: var(--ink);
  }
  .card {
    position: absolute;
    left: 265px;
    width: 580px;
    height: 364px;
    border-radius: 20px;
    overflow: hidden;
  }
  .card--front { top: 225px; background: var(--paper); }
  .card--back { top: 616px; background: var(--accent); }

  /* Front */
  .brand-mark {
    position: absolute;
    border-radius: 50%;
    background: var(--ink);
  }
  .card--front .brand-mark { left: 150px; top: 128px; width: 72px; height: 72px; }
  .brand-name {
    position: absolute;
    font-weight: 800;
    color: var(--ink);
    letter-spacing: 0.5px;
    white-space: nowrap;
  }
  .card--front .brand-name { left: 133px; top: 248px; font-size: 22px; }
  .divider {
    position: absolute;
    left: 295px; top: 111px;
    width: 1.5px; height: 174px;
    background: var(--ink);
  }
  .contact { position: absolute; left: 318px; top: 110px; }
  .contact__name { font-size: 21px; font-weight: 800; line-height: 1.2; }
  .contact__title { font-size: 13px; font-weight: 500; margin-top: 1px; }
  .contact__address { font-size: 13.5px; line-height: 16px; margin-top: 21px; }
  .contact__list { list-style: none; margin-top: 10px; }
  .contact__item {
    display: flex; align-items: center;
    font-size: 13.5px; height: 25px;
  }
  .contact__icon { width: 12px; height: 12px; margin-right: 9px; margin-left: 1px; fill: var(--ink); }

  /* Back */
  .backdrop-shape {
    position: absolute;
    left: -150px; top: -40px;
    width: 330px; height: 440px;
    border-radius: 50%;
    background: var(--accent-deep);
    opacity: 0.85;
  }
  .card--back .brand-mark { left: 204px; top: 88px; width: 118px; height: 118px; }
  .card--back .brand-name { left: 222px; top: 280px; font-size: 34px; }
</style>
</head>
<body>
  <section class="card card--front" aria-label="Business card front">
    <div class="brand-mark" aria-hidden="true"></div>
    <div class="brand-name">VOLMAREX</div>
    <div class="divider"></div>
    <div class="contact">
      <p class="contact__name">Daniel Harlow</p>
      <p class="contact__title">Managing Director</p>
      <p class="contact__address">240 Ridge Hollow Lane<br>Fairview, TN 37062</p>
      <ul class="contact__list">
        <li class="contact__item">
          <svg class="contact__icon" viewBox="0 0 24 24" aria-hidden="true"><path d="M6.6 10.8a15.1 15.1 0 0 0 6.6 6.6l2.2-2.2a1 1 0 0 1 1-.25 11.4 11.4 0 0 0 3.6.57 1 1 0 0 1 1 1V20a1 1 0 0 1-1 1A17 17 0 0 1 3 4a1 1 0 0 1 1-1h3.5a1 1 0 0 1 1 1c0 1.25.2 2.45.57 3.57a1 1 0 0 1-.25 1z"/></svg>
          800.555.0147
        </li>
        <li class="contact__item">
          <svg class="contact__icon" viewBox="0 0 24 24" aria-hidden="true"><path d="M2 5h20v14H2z M2 6l10 7 10-7" /><path d="M2 5l10 7 10-7z" fill="#fff"/></svg>
          info@volmarex.com
        </li>
        <li class="contact__item">
          <svg class="contact__icon" viewBox="0 0 24 24" aria-hidden="true"><circle cx="12" cy="12" r="10"/><path d="M7 6c2 1 3 3 2 5s-3 2-3 4M15 4c-1 2 0 4 2 5s3 3 2 6" stroke="#fff" stroke-width="1.6" fill="none"/></svg>
          www.volmarex.com
        </li>
      </ul>
    </div>
  </section>

  <section class="card card--back" aria-label="Business card back">
    <div class="backdrop-shape" aria-hidden="true"></div>
    <div class="brand-mark" aria-hidden="true"></div>
    <div class="brand-name">VOLMAREX</div>
  </section>
</body>
</html>
```